Custom Harbor Blinds ( I have a logo)

We need a medium van wrap design (Norvik talora cargo van 2500 regular base 4 doors) for small business. We develop custom windows treatmeants ( blind...

Target Market(s)

Installations and sales of window coverings

Industry/Entity Type

Business

Requirements
Must have
• Clean description of what we do and the slogan of the company ( Your vision, our quality
Nice to have
• Clean and professional look, free consultation , fully insured
Should not have
• To many pictures, we are more interested on customers focusing in what kind of work we perform than looking an a gallery on wheels

```html
<!DOCTYPE html>
<html lang="en">
<head>
<meta charset="utf-8">
<title>Custom Harbor Blinds – Van Wrap Side Panel</title>
<link rel="stylesheet" href="https://fonts.googleapis.com/css2?family=Bebas+Neue&display=swap">
<style>
  :root {
    --backdrop: #d6d6d6;
    --wrap-white: #ffffff;
    --sun-yellow: #fdc92c;
    --sun-yellow-light: #ffe27a;
    --coral: #f26a46;
    --coral-soft: #f48a6c;
    --peach: #f9b7a3;
    --ink-grey: #6f6f6f;
    --photo-light: #e9edf0;
    --photo-mid: #c9d2d8;
    --photo-warm: #d9c3a8;
    --trim: #2b2b2b;
  }
  * { margin: 0; padding: 0; box-sizing: border-box; }
  html, body {
    width: 1200px;
    height: 869px;
    overflow: hidden;
    background: var(--backdrop);
  }
  .canvas {
    position: relative;
    width: 1200px;
    height: 869px;
    font-family: "Bebas Neue", "Oswald", sans-serif;
  }
  .wrap-side {
    position: absolute;
    left: 60px;
    top: 150px;
    width: 1080px;
    height: 560px;
  }
  .wrap-art { position: absolute; inset: 0; }
  .services {
    position: absolute;
    left: 370px;
    top: 34px;
    color: var(--wrap-white);
    font-size: 52px;
    line-height: 1.04;
    letter-spacing: -0.3px;
    list-style: none;
  }
  .brand {
    position: absolute;
    right: 40px;
    top: 120px;
    display: flex;
    align-items: center;
    gap: 16px;
  }
  .brand-mark {
    width: 56px;
    height: 56px;
    border: 5px solid var(--coral-soft);
  }
  .brand-name {
    color: var(--ink-grey);
    font-size: 38px;
    line-height: 0.98;
  }
  .slogan {
    position: absolute;
    right: 40px;
    top: 254px;
    color: var(--coral);
    font-size: 24px;
    letter-spacing: 0.5px;
    white-space: nowrap;
  }
  .call {
    position: absolute;
    left: 600px;
    top: 350px;
    color: var(--coral);
  }
  .call-label { font-size: 48px; line-height: 1; }
  .call-phone { font-size: 80px; line-height: 0.95; letter-spacing: 1px; }
</style>
</head>
<body>
<main class="canvas">
  <section class="wrap-side">
    <svg class="wrap-art" width="1080" height="560" viewBox="0 0 1080 560">
      <defs>
        <linearGradient id="yellow-fade" x1="0" y1="0" x2="0" y2="1">
          <stop offset="0" stop-color="var(--sun-yellow-light)"/>
          <stop offset="0.5" stop-color="var(--sun-yellow)"/>
        </linearGradient>
        <linearGradient id="photo-tone" x1="0" y1="0" x2="1" y2="1">
          <stop offset="0" stop-color="var(--photo-light)"/>
          <stop offset="0.6" stop-color="var(--photo-mid)"/>
          <stop offset="1" stop-color="var(--photo-warm)"/>
        </linearGradient>
      </defs>
      <rect class="panel-base" width="1080" height="560" fill="var(--wrap-white)"/>
      <rect class="interior-photo" x="330" y="300" width="750" height="260" fill="url(#photo-tone)" role="img" aria-label="Photo of a bright living room with installed window blinds"/>
      <rect class="front-yellow" width="340" height="560" fill="url(#yellow-fade)"/>
      <polygon class="front-peach" points="0,0 180,0 0,120" fill="var(--peach)"/>
      <polygon class="front-coral-band" points="0,400 340,330 340,470 0,560" fill="var(--coral)"/>
      <polygon class="services-block" points="330,0 960,0 800,120 720,300 330,300" fill="var(--coral-soft)"/>
      <polygon class="services-tip" points="960,0 1040,0 800,120" fill="var(--coral-soft)" opacity="0.55"/>
      <line class="door-seam" x1="340" y1="0" x2="340" y2="560" stroke="var(--trim)" stroke-opacity="0.15" stroke-width="2"/>
      <line class="slide-seam" x1="720" y1="300" x2="720" y2="560" stroke="var(--trim)" stroke-opacity="0.12" stroke-width="2"/>
      <rect class="rub-strip" x="0" y="500" width="1080" height="40" fill="var(--trim)" opacity="0.85"/>
    </svg>

    <ul class="services">
      <li>Custom Shades</li>
      <li>Window Treatments</li>
      <li>Roman Blinds</li>
      <li>And More!</li>
    </ul>

    <div class="brand">
      <span class="brand-mark"></span>
      <span class="brand-name">Custom<br>Harbor<br>Blinds</span>
    </div>
    <p class="slogan">Your vision, our quality</p>

    <div class="call">
      <p class="call-label">Call Us Now</p>
      <p class="call-phone">555-014-2273</p>
    </div>
  </section>
</main>
</body>
</html>
```